Briefpapier und Visitenkarten für Bayerisches Gasthaus mit Zimmer
Zielgruppe
Traditionelle Gaststätte im Zentrum einer Kleinstadt in Bayern. Direkt am Marktplatz. 10 Gästezimmer.
Bayerisch. Traditionell. Von junger Geschäftsführerin geführt, mit jungem Personal. Wir haben das Objekt erst vor Kurzem erworben und fangen gerade an.
Gerichte: Braten, Steaks, Brotzeiten, vegetarische und VEGANE Speisen
Getränke: Sehr bierlastig. Es war früher ein Brauereigasthaus. Heute gibts auch eine kleine feine Weinkarte.
Zielgruppe sind Einheimische und Touristen. Im Sommer kommen Radfahrer und Wanderer. Besonders angesprochen werden auch Kinder. Es gibt eine großzügige Spielecke.
Aufgabenstellung
Das Gasthaus heißt Kraner. Daher spielt der Kraner im Design auch eine wichtige Rolle.
Nachdem wir sehr familienorientiert sind, könnte ich mir auch eine Kraner-Familie vorstellen.
Visitenkarten und Briefpapier sollen alle wichtigen Infos enthalten, aber dabei sehr klar gehalten werden und nicht überladen sein. Mir ist ein schlichtes und ansprechendes Design wichtig. Es soll nicht verspielt sein.
Hier ist die Homepage:
www.kraner-muelbach.de
Info auf Briefpapier:
GASTHAUS KRANER
Brandauer GmbH
Als Info auf Visitenkarte:
Gasthaus Kraner

```html
<!DOCTYPE html>
<html lang="de">
<head>
<meta charset="utf-8">
<title>Gasthaus Kraner – Visitenkarten</title>
<link rel="stylesheet" href="https://fonts.googleapis.com/css2?family=Cinzel:wght@400;500&family=Barlow:wght@400;500&display=swap">
<style>
  :root{
    --stage:#747577;
    --green:#a5c520;
    --green-pale:#d6e6a4;
    --charcoal:#575757;
    --grey-text:#6e6e6e;
    --title-grey:#9a9a9a;
    --white:#ffffff;
  }
  *{box-sizing:border-box;margin:0;padding:0}
  html,body{width:1200px;height:1008px;overflow:hidden;background:var(--stage)}
  body{position:relative;font-family:"Barlow",Arial,sans-serif}
  .card{position:absolute;width:408px;height:259px;overflow:hidden;background:var(--white)}
  .card--green-top{left:120px;top:172px}
  .card--dark-top{left:672px;top:172px}
  .card--green-centered{left:120px;top:577px}
  .card--white-centered{left:672px;top:577px}
  .abs{position:absolute}

  .brand-name{font-family:"Cinzel",Georgia,serif;font-weight:500;letter-spacing:2px;line-height:1}
  .tagline{font-family:"Barlow",Arial,sans-serif;letter-spacing:1px}

  .contact{font-size:12.5px;line-height:18.7px;letter-spacing:.3px}
  .contact-row{position:relative;padding-left:18px;white-space:nowrap}
  .contact-row .icon{position:absolute;left:0;top:3px;width:12px;height:12px}

  /* card 1 */
  .card--green-top .head{left:0;top:0;width:408px;height:130px;background:var(--green)}
  .card--green-top .rule{left:0;top:130px;width:408px;height:2px;background:var(--green-pale)}
  .card--green-top .body{left:0;top:132px;width:408px;height:117px;background:var(--green)}
  .card--green-top .brand-name{right:24px;top:30px;text-align:right;color:var(--white);font-size:29px}
  .card--green-top .tagline{right:29px;top:90px;color:var(--white);font-size:11.5px}
  .card--green-top .mark{left:62px;top:30px;width:62px;height:62px;border-radius:50%;background:var(--green-pale)}
  .card--green-top .contact{color:var(--white)}
  .card--green-top .icon{fill:var(--white)}

  /* card 2 */
  .card--dark-top .head{left:0;top:0;width:408px;height:125px;background:var(--charcoal)}
  .card--dark-top .rule{left:0;top:127px;width:408px;height:3px;background:var(--green)}
  .card--dark-top .foot{left:0;bottom:0;width:408px;height:10px;background:var(--green)}
  .card--dark-top .brand-name{right:32px;top:32px;text-align:right;color:var(--title-grey);font-size:29px}
  .card--dark-top .tagline{right:36px;top:90px;color:var(--title-grey);font-size:11.5px}
  .card--dark-top .mark{left:62px;top:30px;width:62px;height:62px;border-radius:50%;background:var(--green)}
  .card--dark-top .contact{color:var(--grey-text)}
  .card--dark-top .icon{fill:var(--green)}

  .col-left{left:28px;top:182px}
  .col-right{left:206px;top:182px}

  /* card 3 */
  .card--green-centered .field{left:0;top:0;width:408px;height:210px;background:var(--green)}
  .card--green-centered .mark{left:174px;top:28px;width:60px;height:60px;border-radius:50%;background:var(--charcoal)}
  .card--green-centered .brand-name{left:0;width:408px;top:130px;text-align:center;color:var(--white);font-size:19px;line-height:21px;font-weight:400;letter-spacing:2.5px}
  .card--green-centered .divider{left:127px;top:177px;width:154px;height:2px;background:var(--charcoal);border-radius:1px}
  .card--green-centered .tagline{left:0;width:408px;top:184px;text-align:center;color:var(--white);font-size:10.5px;letter-spacing:.2px}
  .card--green-centered .footer-info{left:0;width:408px;top:216px;text-align:center;color:var(--grey-text);font-size:11px;line-height:15.5px;letter-spacing:.2px}
  .dot{display:inline-block;width:4px;height:4px;border-radius:50%;background:var(--green);vertical-align:middle;margin:0 3px}

  /* card 4 */
  .card--white-centered .mark{left:68px;top:30px;width:60px;height:60px;border-radius:50%;background:var(--green)}
  .card--white-centered .brand-name{left:0;width:196px;top:141px;text-align:center;color:var(--grey-text);font-size:20px;line-height:21.5px;font-weight:400;letter-spacing:2.5px}
  .card--white-centered .divider{left:16px;top:188px;width:164px;height:2px;background:var(--green);border-radius:1px}
  .card--white-centered .tagline{left:0;width:196px;top:199px;text-align:center;color:var(--grey-text);font-size:10.5px;line-height:14.5px;letter-spacing:1.3px}
  .card--white-centered .contact{left:212px;top:38px;color:var(--grey-text);font-size:11.5px;line-height:19px}
  .card--white-centered .icon{fill:var(--green)}
  .gap{height:5px}
</style>
</head>
<body>
<svg width="0" height="0" style="position:absolute" aria-hidden="true">
  <defs>
    <symbol id="i-pin" viewBox="0 0 12 12"><path d="M6 0a4 4 0 0 0-4 4c0 3 4 8 4 8s4-5 4-8a4 4 0 0 0-4-4zm0 5.6A1.6 1.6 0 1 1 6 2.4a1.6 1.6 0 0 1 0 3.2z"/></symbol>
    <symbol id="i-phone" viewBox="0 0 12 12"><path d="M3 .5 5 3 3.8 4.6c.6 1.4 1.9 2.8 3.6 3.6L9 7l2.5 2-1.3 2.3C5.5 11 1 6.5.7 1.8z"/></symbol>
    <symbol id="i-mail" viewBox="0 0 12 12"><path d="M6 .5a5.5 5.5 0 1 0 3 10.1l-.6-1A4.3 4.3 0 1 1 10.3 6v.6c0 .7-.4 1.1-.9 1.1s-.9-.4-.9-1.1V3.4H7.4v.4A2.6 2.6 0 1 0 7.6 7.6 2 2 0 0 0 9.4 8.9c1.3 0 2.1-1 2.1-2.3V6A5.5 5.5 0 0 0 6 .5zm-.2 7a1.5 1.5 0 1 1 0-3 1.5 1.5 0 0 1 0 3z"/></symbol>
    <symbol id="i-web" viewBox="0 0 12 12"><path d="M6 .5a5.5 5.5 0 1 0 0 11 5.5 5.5 0 0 0 0-11zm3.9 4.8H8.2A8 8 0 0 0 7.5 2a4.3 4.3 0 0 1 2.4 3.3zM6 1.8c.5.8.9 2 1 3.5H5c.1-1.5.5-2.7 1-3.5zM4.5 2a8 8 0 0 0-.7 3.3H2.1A4.3 4.3 0 0 1 4.5 2zM2.1 6.7h1.7A8 8 0 0 0 4.5 10a4.3 4.3 0 0 1-2.4-3.3zM6 10.2c-.5-.8-.9-2-1-3.5h2c-.1 1.5-.5 2.7-1 3.5zm1.5-.2a8 8 0 0 0 .7-3.3h1.7A4.3 4.3 0 0 1 7.5 10z"/></symbol>
  </defs>
</svg>

<!-- Card 1: green header -->
<section class="card card--green-top">
  <div class="abs head"></div>
  <div class="abs rule"></div>
  <div class="abs body"></div>
  <div class="abs mark"></div>
  <div class="abs brand-name">GASTHAUS<br>KRANER</div>
  <div class="abs tagline">Mülbach im Talgrund</div>
  <div class="abs contact col-left">
    <div class="contact-row"><svg class="icon"><use href="#i-pin"/></svg>Brandauer GmbH</div>
    <div class="contact-row">Marktplatz 12</div>
    <div class="contact-row">84099 Mülbach</div>
  </div>
  <div class="abs contact col-right">
    <div class="contact-row"><svg class="icon"><use href="#i-phone"/></svg>09871 4630</div>
    <div class="contact-row"><svg class="icon"><use href="#i-mail"/></svg>info@kraner-muelbach.de</div>
    <div class="contact-row"><svg class="icon"><use href="#i-web"/></svg>www.kraner-muelbach.de</div>
  </div>
</section>

<!-- Card 2: charcoal header -->
<section class="card card--dark-top">
  <div class="abs head"></div>
  <div class="abs rule"></div>
  <div class="abs foot"></div>
  <div class="abs mark"></div>
  <div class="abs brand-name">GASTHAUS<br>KRANER</div>
  <div class="abs tagline">Mülbach im Talgrund</div>
  <div class="abs contact col-left">
    <div class="contact-row"><svg class="icon"><use href="#i-pin"/></svg>Brandauer GmbH</div>
    <div class="contact-row">Marktplatz 12</div>
    <div class="contact-row">84099 Mülbach</div>
  </div>
  <div class="abs contact col-right">
    <div class="contact-row"><svg class="icon"><use href="#i-phone"/></svg>09871 4630</div>
    <div class="contact-row"><svg class="icon"><use href="#i-mail"/></svg>info@kraner-muelbach.de</div>
    <div class="contact-row"><svg class="icon"><use href="#i-web"/></svg>www.kraner-muelbach.de</div>
  </div>
</section>

<!-- Card 3: green centred -->
<section class="card card--green-centered">
  <div class="abs field"></div>
  <div class="abs mark"></div>
  <div class="abs brand-name">GASTHAUS<br>KRANER</div>
  <div class="abs divider"></div>
  <div class="abs tagline">MÜLBACH IM TALGRUND</div>
  <div class="abs footer-info">
    GASTHAUS KRANER<span class="dot"></span>Brandauer GmbH<span class="dot"></span>Marktplatz 12<span class="dot"></span>84099 Mülbach<br>
    Tel. 09871 4630<span class="dot"></span>info@kraner-muelbach.de<span class="dot"></span>www.kranermuelbach.de
  </div>
</section>

<!-- Card 4: white centred -->
<section class="card card--white-centered">
  <div class="abs mark"></div>
  <div class="abs brand-name">GASTHAUS<br>KRANER</div>
  <div class="abs divider"></div>
  <div class="abs tagline">MÜLBACH<br>IM TALGRUND</div>
  <div class="abs contact">
    <div class="contact-row"><svg class="icon"><use href="#i-pin"/></svg>GASTHAUS KRANER</div>
    <div class="gap"></div>
    <div class="contact-row">Brandauer GmbH</div>
    <div class="contact-row">Marktplatz 12</div>
    <div class="contact-row">84099 Mülbach</div>
    <div class="gap"></div>
    <div class="contact-row"><svg class="icon"><use href="#i-phone"/></svg>09871 4630</div>
    <div class="gap"></div>
    <div class="contact-row"><svg class="icon"><use href="#i-mail"/></svg>info@kraner-muelbach.de</div>
    <div class="contact-row"><svg class="icon"><use href="#i-web"/></svg>www.kraner-muelbach.de</div>
  </div>
</section>
</body>
</html>
```